Scholarly Pathways - educational consulting

I am beginning an educational consultation business - focusing on Tribal (Native American Indian) Communities, but will work with anyone. I have work experience in K-12 and Higher Education. Special Education - transition from school to work. Advising and facilitating with academic skills in higher education. I have a BS - Special Education, Masters - Educational Administration and working on a PhD in Higher Education. Also completing PMB approved certification as an Academic Life Coach

Target Market(s)

K12 college bound students and parents, Kinfolk Crossings college bound students and families, special education college bound students and parents

Industry/Entity Type

Business

Contact Information for Business Card

Marnie Odell Fenwick. PO Box 417, Maple Fork, OK 74099. (918) 555-0293. marnie@scholarlypathways.example

Requirements
Must have
• Scholarly Pathways is the name of the business - Kinfolk Crossings is a focus area
Nice to have
• Tourquoise would be nice. I do not have a logo yet

```html
<!DOCTYPE html>
<html lang="en">
<head>
<meta charset="utf-8">
<title>Scholarly Pathways – Business Card</title>
<link rel="stylesheet" href="https://fonts.googleapis.com/css2?family=Open+Sans:wght@400;600;700&display=swap">
<style>
  :root {
    --stage: #8f8f8f;
    --stage-light: #b4b4b4;
    --card-white: #ffffff;
    --ink: #141414;
    --dark-top: #2a2d31;
    --dark-bottom: #0f1012;
    --turquoise: #1e9fd0;
    --text-light: #f2f2f2;
    --divider: #9a9a9a;
  }
  * { box-sizing: border-box; margin: 0; padding: 0; }
  html, body { width: 1200px; height: 900px; overflow: hidden; }
  body {
    font-family: "Open Sans", sans-serif;
    background: radial-gradient(ellipse at 50% 35%, var(--stage-light), var(--stage) 75%);
  }
  .card-set {
    position: absolute;
    top: 295px;
    left: 40px;
    display: flex;
    gap: 40px;
  }
  .card {
    width: 540px;
    height: 310px;
    border-radius: 22px;
    overflow: hidden;
    position: relative;
    box-shadow: 0 14px 30px rgba(0,0,0,0.35);
  }

  /* Front */
  .card-front { background: linear-gradient(var(--dark-top), var(--dark-bottom)); }
  .front-header {
    height: 150px;
    background: var(--card-white);
    display: flex;
    align-items: center;
    justify-content: center;
    gap: 14px;
  }
  .accent-band { height: 10px; background: var(--turquoise); }
  .brand-dot {
    width: 44px; height: 44px; border-radius: 50%;
    background: var(--turquoise);
    flex: none;
  }
  .brand-name {
    font-weight: 700;
    font-size: 30px;
    color: var(--ink);
    letter-spacing: -0.3px;
    white-space: nowrap;
  }
  .front-details {
    display: flex;
    align-items: center;
    height: 150px;
    padding: 0 12px 8px 12px;
  }
  .person {
    flex: none;
    width: 214px;
    text-align: right;
    padding-right: 10px;
    white-space: nowrap;
  }
  .person-name { font-size: 18px; font-weight: 600; color: var(--turquoise); }
  .person-title { font-size: 13px; color: var(--text-light); margin-top: 2px; }
  .detail-divider {
    flex: none;
    width: 1px; height: 84px; background: var(--divider);
    margin-right: 10px;
  }
  .contact-list { list-style: none; }
  .contact-list li {
    display: flex; align-items: center; gap: 6px;
    font-size: 14px; color: var(--text-light);
    line-height: 22px;
    white-space: nowrap;
  }
  .contact-list svg { width: 16px; height: 16px; fill: var(--turquoise); flex: none; }

  /* Back */
  .card-back {
    background: radial-gradient(ellipse at 35% 30%, var(--dark-top), var(--dark-bottom) 80%);
    text-align: center;
    color: var(--text-light);
  }
  .back-brand {
    display: flex; align-items: center; justify-content: center; gap: 12px;
    margin-top: 74px;
  }
  .back-brand .brand-dot { width: 40px; height: 40px; }
  .back-brand .brand-name { color: var(--turquoise); font-size: 28px; }
  .focus-heading {
    font-size: 13px; margin-top: 40px; letter-spacing: 0.1px;
  }
  .focus-list { list-style: none; margin-top: 10px; font-size: 12.5px; line-height: 16px; }
</style>
</head>
<body>
  <main class="card-set">
    <section class="card card-front">
      <header class="front-header">
        <span class="brand-dot"></span>
        <span class="brand-name">Scholarly Pathways</span>
      </header>
      <div class="accent-band"></div>
      <div class="front-details">
        <div class="person">
          <p class="person-name">Marnie Odell Fenwick</p>
          <p class="person-title">Manager</p>
        </div>
        <div class="detail-divider"></div>
        <ul class="contact-list">
          <li>
            <svg viewBox="0 0 24 24" aria-hidden="true"><path d="M6.6 10.8a15.1 15.1 0 0 0 6.6 6.6l2.2-2.2a1 1 0 0 1 1-.25 11.4 11.4 0 0 0 3.6.57 1 1 0 0 1 1 1V20a1 1 0 0 1-1 1A17 17 0 0 1 3 4a1 1 0 0 1 1-1h3.5a1 1 0 0 1 1 1c0 1.25.2 2.45.57 3.57a1 1 0 0 1-.25 1z"/></svg>
            918.555.0293
          </li>
          <li>
            <svg viewBox="0 0 24 24" aria-hidden="true"><path d="M3 5h18a1 1 0 0 1 1 1v12a1 1 0 0 1-1 1H3a1 1 0 0 1-1-1V6a1 1 0 0 1 1-1zm1 2.3V17h16V7.3l-8 5.2z"/></svg>
            marnie@scholarlypathways.example
          </li>
          <li>
            <svg viewBox="0 0 24 24" aria-hidden="true"><path d="M12 3 2 12h3v8h5v-5h4v5h5v-8h3z"/></svg>
            PO Box 417, Maple Fork, OK 74099
          </li>
        </ul>
      </div>
    </section>

    <section class="card card-back">
      <div class="back-brand">
        <span class="brand-dot"></span>
        <span class="brand-name">Scholarly Pathways</span>
      </div>
      <p class="focus-heading">AREAS OF FOCUS: KINFOLK CROSSINGS (NATIVE AMERICAN)</p>
      <ul class="focus-list">
        <li>K12-college, Academic Life Coach,</li>
        <li>K-12 - College Transitions and Special Education</li>
        <li>K-12 - College Transitions</li>
      </ul>
    </section>
  </main>
</body>
</html>
```